Business Card Re-Design...or logo does not look sharp

Hello

We are a start-up and just need someone to help us.

Our colors are: Marlowe Hush pink (yeah I know) and charcoal for the lettering.

I am attaching our logo which needs cleaning up.

We want the JUST the lady ironing on the table (pink) in front, and the background in charcoal. All the business info can be on the back.

Dims on card are 2 x 2''

Also, if you have better ideas....please let us know!

Thanks

Gregory

La Comadre Vapor
4827 Quellbrook Dr Suite B2
El Paso TX 79936
915-555-0148

```html
<!DOCTYPE html>
<html lang="en">
<head>
<meta charset="utf-8">
<title>La Comadre Vapor — Business Cards</title>
<link rel="stylesheet" href="https://fonts.googleapis.com/css2?family=Source+Sans+3:wght@400&display=swap">
<style>
  :root {
    --stage: #ece8e6;
    --charcoal: #242222;
    --charcoal-soft: #2e2b2b;
    --blush: #fcdada;
    --paper-light: #f4f1f1;
    --shadow: rgba(0, 0, 0, 0.22);
  }
  html, body {
    margin: 0;
    padding: 0;
    width: 1200px;
    height: 900px;
    overflow: hidden;
    background: var(--stage);
    font-family: "Source Sans 3", sans-serif;
  }
  .canvas {
    position: relative;
    width: 1200px;
    height: 900px;
  }
  .card {
    position: absolute;
    width: 520px;
    height: 290px;
    box-shadow: 0 6px 18px var(--shadow);
    overflow: hidden;
  }
  /* Front */
  .card-front {
    left: 110px;
    top: 120px;
    background: var(--charcoal);
  }
  .front-texture {
    position: absolute;
    inset: 0;
    background: radial-gradient(ellipse at 80% 75%, var(--charcoal-soft), var(--charcoal) 60%);
  }
  .brand-mark {
    position: absolute;
    inset: 0;
    display: flex;
    align-items: center;
    justify-content: center;
    gap: 14px;
  }
  .brand-dot {
    width: 22px;
    height: 22px;
    border-radius: 50%;
    background: var(--blush);
  }
  .brand-name {
    color: var(--blush);
    font-size: 34px;
    font-weight: 400;
    letter-spacing: 0.5px;
  }
  /* Back */
  .card-back {
    left: 570px;
    top: 490px;
    background: var(--blush);
  }
  .info-band {
    position: absolute;
    left: 0;
    right: 0;
    top: 70px;
    height: 82px;
    background: var(--charcoal);
    box-shadow: 0 3px 4px rgba(0,0,0,0.25);
  }
  .company-name {
    position: absolute;
    left: 0;
    right: 0;
    top: 6px;
    margin: 0;
    text-align: center;
    color: var(--paper-light);
    font-size: 40px;
    font-weight: 400;
    line-height: 48px;
  }
  .contact-line {
    position: absolute;
    left: 14px;
    right: 10px;
    top: 56px;
    margin: 0;
    color: var(--paper-light);
    font-size: 15.5px;
    line-height: 18px;
    white-space: nowrap;
  }
</style>
</head>
<body>
<main class="canvas">
  <section class="card card-front" aria-label="Card front">
    <div class="front-texture" role="img" aria-label="Faint charcoal flourish pattern"></div>
    <div class="brand-mark">
      <span class="brand-dot"></span>
      <span class="brand-name">La Comadre Vapor</span>
    </div>
  </section>

  <section class="card card-back" aria-label="Card back">
    <div class="info-band">
      <h1 class="company-name">La Comadre Vapor</h1>
      <p class="contact-line">4827 Quellbrook Dr Suite B2 El Paso TX 79936 915-555-0148</p>
    </div>
  </section>
</main>
</body>
</html>
```